4x6 -ish post card to let the neighborhood know where here.

Hi All, I opened a high end wine & spirits shop and am looking to get out some sort of a 4x6 postcard a flyer to let people know where in the area. Looking for something clean cut that can maybe incorporate a few pictures from our store on along the top and our logo. Ideally a white-ish background.

```html
<!DOCTYPE html>
<html lang="en">
<head>
<meta charset="utf-8">
<title>Stonebrook Wine &amp; Spirits — Postcard</title>
<link rel="stylesheet" href="https://fonts.googleapis.com/css2?family=Cinzel:wght@500;600&display=swap">
<style>
  :root {
    --page-bg: #e4e4e4;
    --card-white: #ffffff;
    --gold: #b8862b;
    --gold-light: #e6b85a;
    --gold-wash: #efc56a;
    --bronze-dark: #8a5a14;
    --bronze-mid: #c08a2e;
    --storefront-grey: #d9d9d9;
    --photo-wood: #6b4a32;
    --photo-dark: #2a2a2e;
    --photo-frame: #c44a5a;
    --text-white: #ffffff;
  }
  * { box-sizing: border-box; margin: 0; padding: 0; }
  html, body {
    width: 1200px;
    height: 1177px;
    overflow: hidden;
    background: var(--page-bg);
  }
  .postcard {
    position: absolute;
    left: 40px;
    top: 220px;
    width: 1120px;
    height: 738px;
    background: var(--card-white);
    overflow: hidden;
  }
  .storefront-backdrop {
    position: absolute;
    left: 34px;
    top: 32px;
    width: 1052px;
    height: 440px;
    background: linear-gradient(180deg, #cfcfcf 0%, #e2e2e2 55%, rgba(255,255,255,0) 100%),
                linear-gradient(90deg, #d2d2d2 0%, #ececec 50%, #d6d6d6 100%);
    opacity: 0.75;
  }
  .gold-wash {
    position: absolute;
    left: 34px;
    top: 440px;
    width: 1052px;
    height: 268px;
    background:
      linear-gradient(180deg, rgba(255,255,255,1) 0%, rgba(255,255,255,0) 18%, rgba(255,255,255,0) 78%, rgba(255,255,255,1) 100%),
      linear-gradient(90deg, #f0c262 0%, #f4cf7e 40%, #eec06a 75%, #f6d99a 100%);
    opacity: 0.85;
  }
  .frame-outer {
    position: absolute;
    inset: 20px 22px 20px 22px;
    border: 2px solid var(--gold);
  }
  .frame-inner {
    position: absolute;
    inset: 34px 36px 34px 36px;
    border: 1.5px solid var(--gold);
  }
  .brand-name {
    position: absolute;
    left: 0;
    right: 0;
    top: 100px;
    text-align: center;
    font-family: "Cinzel", serif;
    font-weight: 600;
    color: var(--gold);
    line-height: 1;
  }
  .brand-name .brand-primary {
    display: block;
    font-size: 90px;
    letter-spacing: 1px;
  }
  .brand-name .brand-secondary {
    display: block;
    font-size: 50px;
    letter-spacing: 3px;
    margin-top: 14px;
  }
  .gallery-box {
    position: absolute;
    left: 99px;
    top: 330px;
    width: 919px;
    height: 300px;
    background: var(--card-white);
    border: 1.5px solid var(--gold);
    box-shadow: 0 2px 6px rgba(0,0,0,0.12);
  }
  .store-photo {
    position: absolute;
    top: 11px;
    height: 236px;
    border: 2px solid var(--photo-frame);
  }
  .store-photo--entrance {
    left: 14px;
    width: 437px;
    background: linear-gradient(180deg, var(--photo-wood) 0%, #3a3236 30%, var(--photo-dark) 60%, #8d8a86 100%);
  }
  .store-photo--aisle {
    left: 459px;
    width: 445px;
    background: linear-gradient(180deg, #2e2c30 0%, var(--photo-dark) 45%, #4a4448 75%, #9a9794 100%);
  }
  .contact-bar {
    position: absolute;
    left: 14px;
    top: 255px;
    width: 890px;
    height: 32px;
    background: linear-gradient(90deg, var(--bronze-dark) 0%, var(--bronze-mid) 35%, #d9a443 50%, var(--bronze-mid) 65%, var(--bronze-dark) 100%);
    color: var(--text-white);
    font-family: "Cinzel", serif;
    font-weight: 500;
    font-size: 18px;
    letter-spacing: 0.3px;
    display: flex;
    align-items: center;
    justify-content: center;
    white-space: nowrap;
  }
  .contact-bar .divider { margin: 0 10px; }
</style>
</head>
<body>
  <main class="postcard">
    <div class="storefront-backdrop" role="img" aria-label="Faded photo of the shop's storefront with its awning"></div>
    <div class="gold-wash" role="img" aria-label="Soft gold watercolor wash"></div>
    <div class="frame-outer"></div>
    <div class="frame-inner"></div>

    <h1 class="brand-name">
      <span class="brand-primary">STONEBROOK</span>
      <span class="brand-secondary">WINE &amp; SPIRITS</span>
    </h1>

    <section class="gallery-box">
      <div class="store-photo store-photo--entrance" role="img" aria-label="Photo of the shop interior with wine racks and wooden ceiling"></div>
      <div class="store-photo store-photo--aisle" role="img" aria-label="Photo of a long display rack of wine bottles"></div>
      <p class="contact-bar">
        ADDRESS STREET NAME CITY ZIP CODE<span class="divider">|</span>PH: 987654321<span class="divider">|</span>STONEBROOKWINE.COM
      </p>
    </section>
  </main>
</body>
</html>
```